Velmoria - 3D medical animations and high end visual content

Our company creates high end visual content and animations for medical global companies.
Our website - www.velmoria-studio.example
We would like to have an amazing business card for our CEO that he can use in the following exhebitions he is going to attend.
It is very important that the design will be memorable and diffrent. It has to reflect our brand design (you can have it from our website)
We would like to transmit innovation, prestige, luxury, aesthetics.
The card has to be Double Sided

Target Market(s)

Marketing managers in medical global companys

Industry/Entity Type

It Company

Contact Information for Business Card

Requirements
Nice to have
• It is very important that the design will be memorable and diffrent. It has to reflect our brand design (you can have it from our website)

```html
<!DOCTYPE html>
<html lang="en">
<head>
<meta charset="utf-8">
<title>Velmoria – Business Card</title>
<link href="https://fonts.googleapis.com/css2?family=Montserrat:wght@500;600&family=Open+Sans:wght@400;700&display=swap" rel="stylesheet">
<style>
  :root {
    --backdrop: #d9d6d3;
    --card-deep: #04080c;
    --card-glow: #123247;
    --ink-white: #f2f5f7;
    --ink-soft: #c9d2d8;
    --accent-teal: #2a9bb5;
    --accent-gold: #e0b21c;
    --rule: #8fa3ae;
  }
  * { margin: 0; padding: 0; box-sizing: border-box; }
  html, body { width: 1200px; height: 716px; overflow: hidden; }
  body {
    background: var(--backdrop);
    display: flex;
    align-items: center;
    justify-content: center;
    gap: 40px;
    font-family: "Open Sans", Arial, sans-serif;
  }
  .card {
    position: relative;
    width: 540px;
    height: 309px;
    border-radius: 10px;
    background:
      radial-gradient(ellipse at 50% 0%, var(--card-glow) 0%, rgba(18,50,71,0) 65%),
      var(--card-deep);
    box-shadow: 0 12px 30px rgba(0,0,0,0.35);
    overflow: hidden;
  }
  /* Front */
  .card-front { display: flex; align-items: center; justify-content: center; }
  .brand-lockup { display: flex; align-items: center; gap: 14px; }
  .brand-dot {
    width: 16px; height: 16px; border-radius: 50%;
    background: var(--accent-teal);
  }
  .brand-name {
    font-family: "Montserrat", sans-serif;
    font-weight: 600;
    font-size: 44px;
    letter-spacing: 3px;
    text-transform: uppercase;
    color: var(--ink-white);
  }
  /* Back */
  .card-back { padding: 0; }
  .back-mark {
    position: absolute;
    left: 70px; top: 86px;
    width: 120px; height: 120px;
  }
  .contact {
    position: absolute;
    left: 240px; top: 96px;
  }
  .person-name {
    font-weight: 700;
    font-size: 22px;
    color: var(--accent-teal);
    letter-spacing: 0.5px;
  }
  .person-role {
    font-size: 12px;
    color: var(--ink-soft);
    margin: 2px 0 12px;
  }
  .contact-list { list-style: none; }
  .contact-item {
    display: flex; align-items: center; gap: 10px;
    font-size: 13px; line-height: 20px;
    color: var(--ink-white);
  }
  .contact-item svg { width: 12px; height: 12px; flex: none; }
  .web-domain { color: var(--accent-gold); }
</style>
</head>
<body>
  <section class="card card-front" aria-label="Card front">
    <div class="brand-lockup">
      <span class="brand-dot"></span>
      <span class="brand-name">Velmoria</span>
    </div>
  </section>

  <section class="card card-back" aria-label="Card back">
    <svg class="back-mark" viewBox="0 0 120 120" aria-hidden="true">
      <circle cx="60" cy="60" r="50" fill="none" stroke="var(--accent-teal)" stroke-width="6"/>
    </svg>
    <div class="contact">
      <h1 class="person-name">Elan Marcus</h1>
      <p class="person-role">Founder &amp; CEO</p>
      <ul class="contact-list">
        <li class="contact-item">
          <svg viewBox="0 0 12 12"><rect x="3" y="0.5" width="6" height="11" rx="1" fill="none" stroke="var(--accent-teal)" stroke-width="1.3"/><circle cx="6" cy="9.5" r="0.7" fill="var(--accent-teal)"/></svg>
          +000-55-0100123
        </li>
        <li class="contact-item">
          <svg viewBox="0 0 12 12"><path d="M1 4c0-2 2-3 5-3s5 1 5 3v1H8V3.5H4V5H1z M2 6h8v5H2z" fill="var(--accent-teal)"/></svg>
          +000-55-0100456
        </li>
        <li class="contact-item">
          <svg viewBox="0 0 12 12"><rect x="0.5" y="2" width="11" height="8" fill="var(--accent-teal)"/><path d="M0.5 2l5.5 4.5L11.5 2" fill="none" stroke="var(--card-deep)" stroke-width="1"/></svg>
          elan@velmoria-studio.example
        </li>
        <li class="contact-item">
          <svg viewBox="0 0 12 12"><circle cx="6" cy="6" r="5.3" fill="none" stroke="var(--accent-teal)" stroke-width="1.2"/><ellipse cx="6" cy="6" rx="2.3" ry="5.3" fill="none" stroke="var(--accent-teal)" stroke-width="1"/><line x1="0.7" y1="6" x2="11.3" y2="6" stroke="var(--accent-teal)" stroke-width="1"/></svg>
          <span>www.<span class="web-domain">velmoria-studio</span>.example</span>
        </li>
      </ul>
    </div>
  </section>
</body>
</html>
```